New adult online store shopify

I have a new product I'd like to build my shopify store on. It's a product used for foreplay in the bedroom for people who have a temperature play fetish. Testing the boundaries with hot and cold. The glass wands are use to heat wax to put on skin to excite adults I'd like to have a retail store with a log in for wholesalers to log in and place orders
Also needs a plug in to confirm viewers are over 18 years old.
It needs to be classy and descriptive with a clear product message and story but very simple to use

Reason: Deadline extended 5 days

Reason: looking for more options

Target Market(s)

All adults over 18

Industry/Entity Type

Adult

Colors

Designer to choose colors to be used in the design.

Requirements
Must have
• A customer / wholesale login for wholesale purchases
• Templates for abandoned shopping cart emails
• 18+ only visible
Nice to have
• Customer loyalty programme
Should not have
• Cheap Rude images and comment

```html
<!DOCTYPE html>
<html lang="en">
<head>
<meta charset="utf-8">
<title>Emberline — Age Confirmation</title>
<link href="https://fonts.googleapis.com/css2?family=Source+Sans+3:wght@600;700&family=Source+Serif+4:wght@300;400;600&display=swap" rel="stylesheet">
<style>
  :root{
    --header-bg:#8b878b;
    --hero-shade:#7c7779;
    --footer-band:#8a8589;
    --nav-text:#f1eeee;
    --input-bg:#e3dfdf;
    --input-text:#a69c9c;
    --search-bg:#bdb8b9;
    --search-text:#8a7474;
    --wine:#6b1a17;
    --panel:#ffffff;
    --body-text:#7a7474;
    --muted-btn:#6f6b6b;
    --shop-bg:#e0dcdc;
    --shop-text:#8a7474;
  }
  *{box-sizing:border-box;margin:0;padding:0}
  html,body{width:1200px;height:946px;overflow:hidden}
  body{position:relative;background:var(--footer-band);font-family:"Source Serif 4",Georgia,serif}
  .site-header{position:absolute;left:0;top:0;width:1200px;height:215px;background:var(--header-bg)}
  .brand{position:absolute;left:97px;top:148px;font-family:"Source Serif 4",Georgia,serif;font-weight:600;font-size:36px;color:#f0c48a;letter-spacing:1px}
  .account-link{position:absolute;left:890px;top:30px;font-size:17px;font-weight:600;color:var(--nav-text)}
  .cart{position:absolute;left:1053px;top:28px;width:26px;height:24px}
  .search-input{position:absolute;left:656px;top:81px;width:317px;height:52px;background:var(--input-bg);color:var(--input-text);font-size:16px;font-weight:300;padding:17px 17px 0}
  .search-btn{position:absolute;left:1016px;top:81px;width:84px;height:52px;background:var(--search-bg);color:var(--search-text);font-size:19px;font-weight:400;text-align:center;line-height:52px}
  .main-nav{position:absolute;top:160px;font-size:19px;font-weight:600;color:var(--nav-text);letter-spacing:.3px}
  .hero-photo{position:absolute;left:0;top:215px;width:1200px;height:685px;
    background:radial-gradient(ellipse at 25% 40%,#8a5f66 0%,#6f5157 35%,transparent 60%),
               radial-gradient(ellipse at 85% 60%,#7f6066 0%,#6c5a5d 40%,transparent 65%),
               radial-gradient(ellipse at 55% 80%,#76585d 0%,transparent 55%),
               var(--hero-shade)}
  .age-gate{position:absolute;left:279px;top:249px;width:660px;height:384px;background:var(--panel)}
  .age-mark{position:absolute;left:0;width:660px;top:8px;text-align:center;font-family:"Source Sans 3",Arial,sans-serif;font-weight:700;font-size:104px;color:var(--wine);line-height:1.2}
  .age-rule{position:absolute;left:80px;top:126px;width:501px;height:3px;background:var(--wine)}
  .age-message{position:absolute;left:0;top:142px;width:660px;text-align:center;font-weight:300;font-size:29.5px;line-height:47px;color:var(--body-text)}
  .age-btn{position:absolute;top:309px;width:148px;height:47px;font-family:"Source Sans 3",Arial,sans-serif;font-weight:700;font-size:24px;color:#fff;text-align:center;line-height:47px}
  .age-btn.under{left:137px;background:var(--muted-btn)}
  .age-btn.over{left:381px;background:var(--wine)}
  .shop-now{position:absolute;left:442px;top:670px;width:316px;height:63px;background:var(--shop-bg);color:var(--shop-text);font-weight:600;font-size:33px;text-align:center;line-height:63px}
</style>
</head>
<body>
  <header class="site-header">
    <div class="brand">Emberline</div>
    <div class="account-link">Sign up / Sign in</div>
    <svg class="cart" viewBox="0 0 26 24" aria-label="Cart">
      <path d="M1 3h4l3 11h12l3-8H7" fill="none" stroke="#f1eeee" stroke-width="1.5" stroke-linejoin="round"/>
      <circle cx="10" cy="19" r="1.6" fill="none" stroke="#f1eeee" stroke-width="1.3"/>
      <circle cx="18" cy="19" r="1.6" fill="none" stroke="#f1eeee" stroke-width="1.3"/>
      <circle cx="21" cy="4" r="4" fill="#c96b6b"/>
      <text x="21" y="6" font-size="6" fill="#fff" text-anchor="middle" font-family="Arial,sans-serif">1</text>
    </svg>
    <div class="search-input">What are you looking for</div>
    <div class="search-btn">Search</div>
    <nav>
      <span class="main-nav" style="left:549px">HOME</span>
      <span class="main-nav" style="left:642px">CATEGORY</span>
      <span class="main-nav" style="left:781px">HOT</span>
      <span class="main-nav" style="left:852px">SELL</span>
      <span class="main-nav" style="left:929px">BLOG</span>
      <span class="main-nav" style="left:1010px">CONTACT</span>
    </nav>
  </header>

  <div class="hero-photo" role="img" aria-label="Close-up photograph of dark red cherries with water droplets"></div>

  <section class="age-gate">
    <div class="age-mark">18+</div>
    <div class="age-rule"></div>
    <p class="age-message">This website contains content for<br>people 18 and older. Please confirm<br>the information below</p>
    <div class="age-btn under">UNDER 18</div>
    <div class="age-btn over">18+</div>
  </section>

  <div class="shop-now">Shop Now</div>
</body>
</html>
```